依頼詳細
PC版のTOPページと下層1ページのデザイン制作をお願いいたします。
TOPページメイン部分に埋め込み用の動画、サイトマップ、依頼内容詳細.txtをご確認いただき、動画のテイスト(方眼紙やフォントなど)を参考にシンプルで見やすいデザインで制作いただきたいです。
スムーズな連絡と軽微な修正にご対応いただける方へご依頼をさせていただきたいです。
ターゲットは建築資材・家具建具資材・住設機器などを必要とする建築会社様、家具・建具製造会社様などです。
ページ数
2ページ
希望イメージ
シンプル 複雑
単色 カラフル
暗い 明るい
日常 高級
遊び心 厳粛
未来的 伝統的
女性的 男性的
希望する色
青系、茶系、グレー系
納品ファイル
• イラストレーター形式 (.ai)
補足説明
納品ファイルはXDも可です。
-
■ 選んだ理由

動画とのイメージが合っており選ばせていただきました。

■ 提案者全員のお礼・コメント

たくさんのご提案をいただきありがとうございました。
また機会がございましたらよろしくお願いいたします。

```html
<!DOCTYPE html>
<html lang="ja">
<head>
<meta charset="utf-8">
<title>TOBIKENZAI</title>
<link rel="stylesheet" href="https://fonts.googleapis.com/css2?family=Archivo:wght@400;500;700;800&family=Noto+Sans+JP:wght@400;500;700&family=Zen+Kaku+Gothic+New:wght@700&display=swap">
<style>
:root{
  --ink:#2b2624;
  --brown:#8c6b41;
  --paper:#ffffff;
  --tint:#ececeb;
  --tint-dark:#e2e2e1;
  --grid:#d6d6d4;
  --grid-strong:#c9c9c7;
  --rule:#cfcfcf;
  --muted:#6d6a68;
}
*{box-sizing:border-box;margin:0;padding:0}
html,body{width:1200px;height:4044px;overflow:hidden}
body{position:relative;color:var(--ink);font-family:"Noto Sans JP",sans-serif;background-color:var(--tint)}
.graph-paper{
  background-image:
    linear-gradient(var(--grid-strong) 1px,transparent 1px),
    linear-gradient(90deg,var(--grid-strong) 1px,transparent 1px),
    linear-gradient(var(--grid) 1px,transparent 1px),
    linear-gradient(90deg,var(--grid) 1px,transparent 1px);
  background-size:160px 160px,160px 160px,32px 32px,32px 32px;
}
.abs{position:absolute}
.en{font-family:"Archivo",sans-serif}

/* header */
.site-header{left:0;top:0;width:1200px;height:92px;background:var(--paper)}
.brand{left:40px;top:28px;font-family:"Archivo",sans-serif;font-weight:500;font-size:28px;letter-spacing:1px}
.global-nav{right:110px;top:36px;display:flex;gap:34px;font-size:15px;font-weight:500}
.global-nav span:first-child{border-bottom:2px solid var(--brown);padding-bottom:4px}
.menu-icon{right:40px;top:32px;width:34px;height:24px}

/* hero */
.hero-word{left:0;width:1200px;top:150px;text-align:center;font-family:"Archivo",sans-serif;font-weight:500;font-size:178px;letter-spacing:4px;color:transparent;-webkit-text-stroke:2px var(--ink);line-height:1}
.catch{top:600px;left:190px;display:flex;flex-direction:row-reverse;align-items:flex-start;gap:16px}
.catch span{writing-mode:vertical-rl;background:var(--paper);color:var(--brown);font-family:"Zen Kaku Gothic New",sans-serif;font-weight:700;font-size:60px;line-height:1;padding:16px;letter-spacing:6px}
.catch-sub{left:522px;top:640px;writing-mode:vertical-rl;font-family:"Archivo",sans-serif;font-weight:700;font-size:15px;letter-spacing:3px;line-height:1.9}

.panel{background:var(--paper)}
.section-title{font-family:"Archivo",sans-serif;font-weight:800;letter-spacing:2px;line-height:1}
.label-ja{font-size:14px;color:var(--ink)}
.dummy{font-size:14px;line-height:2.1;color:var(--ink)}
.more{display:flex;align-items:center;justify-content:space-between;width:200px;height:42px;padding:0 14px 0 36px;border-bottom:2px solid var(--brown);border-right:2px solid var(--brown);font-family:"Archivo",sans-serif;font-weight:700;font-size:17px}
.more svg{width:34px;height:16px}
.rule-brown{height:3px;background:var(--brown);width:60px}

/* news */
.news-title{writing-mode:vertical-rl;font-size:96px}
.news-list{left:380px;width:710px}
.news-row{display:flex;gap:60px;align-items:center;height:70px;border-bottom:1px solid var(--rule);font-size:14px;position:relative}
.news-row::after{content:"";position:absolute;left:0;bottom:-1px;width:140px;height:2px;background:var(--ink)}
.news-row .date{font-family:"Archivo",sans-serif;font-weight:500;width:120px;padding-left:8px}

/* products */
.product-item{width:210px;text-align:center}
.product-circle{width:200px;height:200px;margin:0 auto;border:2px solid var(--ink);border-radius:50%;display:flex;align-items:center;justify-content:center;background:var(--paper)}
.icon-slot{width:90px;height:90px;border-radius:8px;background:var(--tint-dark)}
.product-name{margin-top:22px;font-size:15px;font-weight:500}

/* audience */
.audience-band{background-color:var(--tint-dark)}
.audience{width:420px;text-align:center}
.audience-icon{width:90px;height:90px;margin:0 auto 18px;background:var(--tint);border-radius:50%}
.audience .kicker{font-family:"Archivo",sans-serif;font-weight:800;font-size:28px;letter-spacing:2px}
.audience h3{font-family:"Archivo",sans-serif;font-weight:800;font-size:46px;letter-spacing:1px;line-height:1.1}
.audience .rule-brown{margin:18px auto}

/* footer */
.site-footer{left:0;top:3770px;width:1200px;height:274px;background:var(--paper)}
.footer-links{display:grid;grid-template-columns:230px 230px;row-gap:20px;font-size:15px}
.footer-links span::before{content:"";display:inline-block;width:12px;height:2px;background:var(--brown);vertical-align:middle;margin-right:10px}
</style>
</head>
<body class="graph-paper">

<header class="site-header abs">
  <div class="brand abs">TOBIKENZAI</div>
  <nav class="global-nav abs"><span>ご挨拶</span><span>新着情報</span><span>取扱商品</span><span>お施主様向け情報</span><span>工務店様向け情報</span><span>採用情報</span></nav>
  <svg class="menu-icon abs" viewBox="0 0 34 24"><rect width="34" height="24" fill="none" stroke="var(--ink)" stroke-width="2"/><path d="M8 8h18M8 12h18M8 16h18" stroke="var(--ink)" stroke-width="2"/></svg>
</header>

<div class="hero-word abs">TOBIKENZAI</div>

<div class="catch abs"><span>ここに</span><span>キャッチコピーが</span><span>入ります。</span></div>
<div class="catch-sub abs">KOKONI CATCH COPY GA<br>HAIRIMASU</div>

<section class="panel abs" style="left:640px;top:640px;width:560px;height:520px">
  <h2 class="section-title abs" style="left:30px;top:140px;font-size:78px">GREETING</h2>
  <div class="rule-brown abs" style="left:400px;top:245px"></div>
  <div class="label-ja abs" style="left:410px;top:262px">ご挨拶</div>
  <p class="dummy abs" style="left:30px;top:300px;width:430px">ここに文字が入ります。ここにテキストが入ります。ここに文字が入ります。ここにテキストが入ります。ここに文字が入ります。ここにテキストが入ります。ここに文字が入ります。ここにテキストが入ります。ここに文字が入ります。</p>
  <div class="more abs" style="left:230px;top:420px">more view
    <svg viewBox="0 0 34 16"><path d="M0 8h22" stroke="var(--ink)" stroke-width="2"/><circle cx="26" cy="8" r="7" fill="none" stroke="var(--ink)" stroke-width="1.5"/><path d="M24 5l3 3-3 3" fill="none" stroke="var(--ink)" stroke-width="1.5"/></svg></div>
</section>

<section class="panel abs" style="left:0;top:1310px;width:1200px;height:420px">
  <h2 class="section-title news-title abs" style="left:110px;top:60px">NEWS</h2>
  <div class="label-ja abs" style="left:228px;top:64px;writing-mode:vertical-rl">新着情報</div>
  <div class="news-list abs" style="top:80px">
    <div class="news-row"><span class="date">2021/00/00</span><span>ここにテキストが入ります。ここに文字が入ります。ここにテキストが入ります。</span></div>
    <div class="news-row"><span class="date">2021/00/00</span><span>ここにテキストが入ります。ここに文字が入ります。ここにテキストが入ります。</span></div>
    <div class="news-row"><span class="date">2021/00/00</span><span>ここにテキストが入ります。ここに文字が入ります。ここにテキストが入ります。</span></div>
  </div>
  <div class="more abs" style="left:870px;top:330px">more view
    <svg viewBox="0 0 34 16"><path d="M0 8h22" stroke="var(--ink)" stroke-width="2"/><circle cx="26" cy="8" r="7" fill="none" stroke="var(--ink)" stroke-width="1.5"/><path d="M24 5l3 3-3 3" fill="none" stroke="var(--ink)" stroke-width="1.5"/></svg></div>
</section>

<section class="abs" style="left:0;top:1780px;width:1200px;height:560px">
  <p class="dummy abs panel" style="left:120px;top:50px;width:410px;padding:10px">ここに文字が入ります。ここにテキストが入ります。ここに文字が入ります。ここにテキストが入ります。</p>
  <h2 class="section-title abs" style="left:665px;top:65px;font-size:82px">PRODUCT</h2>
  <div class="rule-brown abs" style="left:1030px;top:165px"></div>
  <div class="label-ja abs" style="left:1030px;top:180px">取扱商品</div>
  <div class="abs" style="left:80px;top:250px;display:flex;gap:50px">
    <div class="product-item"><div class="product-circle"><div class="icon-slot" role="img" aria-label="作業用ヘルメットのアイコン"></div></div><div class="product-name">ここに商品名が入ります</div></div>
    <div class="product-item"><div class="product-circle"><div class="icon-slot" role="img" aria-label="クレーンと建物のアイコン"></div></div><div class="product-name">ここに商品名が入ります</div></div>
    <div class="product-item"><div class="product-circle"><div class="icon-slot" role="img" aria-label="定規と製図道具のアイコン"></div></div><div class="product-name">ここに商品名が入ります</div></div>
    <div class="product-item"><div class="product-circle"><div class="icon-slot" role="img" aria-label="工具のアイコン"></div></div><div class="product-name">ここに商品名が入ります</div></div>
  </div>
</section>

<section class="audience-band graph-paper abs" style="left:0;top:2390px;width:1200px;height:560px">
  <div class="abs" style="left:598px;top:110px;width:3px;height:340px;background:var(--brown)"></div>
  <div class="audience abs" style="left:150px;top:60px">
    <div class="audience-icon" role="img" aria-label="お施主様を表す人物アイコン"></div>
    <div class="kicker">NEWS FOR</div><h3>CUSTOMER</h3>
    <div class="rule-brown"></div>
    <div class="label-ja">お施主様向け情報</div>
    <p class="dummy" style="margin:14px auto 0;width:250px;text-align:left">ここに文字が入ります。ここに文字が入ります。ここに文字が入ります。</p>
  </div>
  <div class="audience abs" style="left:690px;top:60px">
    <div class="audience-icon" role="img" aria-label="工務店様を表す人物アイコン"></div>
    <div class="kicker">NEWS FOR</div><h3>BUILDING<br>CONTRACTOR</h3>
    <div class="rule-brown"></div>
    <div class="label-ja">工務店様向け情報</div>
    <p class="dummy" style="margin:14px auto 0;width:250px;text-align:left">ここに文字が入ります。ここに文字が入ります。ここに文字が入ります。</p>
  </div>
  <div class="more abs" style="left:180px;top:450px">more view
    <svg viewBox="0 0 34 16"><path d="M0 8h22" stroke="var(--ink)" stroke-width="2"/><circle cx="26" cy="8" r="7" fill="none" stroke="var(--ink)" stroke-width="1.5"/><path d="M24 5l3 3-3 3" fill="none" stroke="var(--ink)" stroke-width="1.5"/></svg></div>
  <div class="more abs" style="left:800px;top:450px">more view
    <svg viewBox="0 0 34 16"><path d="M0 8h22" stroke="var(--ink)" stroke-width="2"/><circle cx="26" cy="8" r="7" fill="none" stroke="var(--ink)" stroke-width="1.5"/><path d="M24 5l3 3-3 3" fill="none" stroke="var(--ink)" stroke-width="1.5"/></svg></div>
</section>

<section class="abs" style="left:0;top:3010px;width:1200px;height:300px">
  <h2 class="section-title abs" style="left:115px;top:70px;font-size:90px">RECRUIT</h2>
  <div class="rule-brown abs" style="left:115px;top:180px"></div>
  <div class="label-ja abs" style="left:115px;top:196px">採用情報</div>
  <p class="dummy abs" style="left:620px;top:60px;width:400px">ここに文字が入ります。ここにテキストが入ります。ここに文字が入ります。ここにテキストが入ります。ここに文字が入ります。</p>
  <div class="more abs" style="left:860px;top:150px">more view
    <svg viewBox="0 0 34 16"><path d="M0 8h22" stroke="var(--ink)" stroke-width="2"/><circle cx="26" cy="8" r="7" fill="none" stroke="var(--ink)" stroke-width="1.5"/><path d="M24 5l3 3-3 3" fill="none" stroke="var(--ink)" stroke-width="1.5"/></svg></div>
</section>

<section class="abs" style="left:0;top:3340px;width:1200px;height:400px">
  <svg class="abs" style="left:555px;top:10px" width="90" height="62" viewBox="0 0 90 62"><rect x="2" y="2" width="86" height="58" fill="var(--paper)" stroke="var(--ink)" stroke-width="3"/><path d="M2 4l43 32 43-32" fill="none" stroke="var(--ink)" stroke-width="3"/></svg>
  <div class="panel abs" style="left:420px;top:100px;width:360px;height:240px;border:2px solid var(--ink);border-top-color:var(--paper)"></div>
  <h2 class="section-title abs" style="left:0;width:1200px;text-align:center;top:185px;font-size:56px">CONTACT</h2>
  <div class="rule-brown abs" style="left:570px;top:255px"></div>
  <div class="label-ja abs" style="left:0;width:1200px;text-align:center;top:272px">お問い合わせ</div>
</section>

<footer class="site-footer abs">
  <div class="brand abs" style="left:40px;top:70px;font-size:32px">TOBIKENZAI</div>
  <div class="footer-links abs" style="left:590px;top:55px">
    <span>ご挨拶</span><span>取扱商品</span>
    <span>新着情報</span><span>採用情報</span>
    <span>お施主様向け情報</span><span>お問い合わせ</span>
    <span>工務店様向け情報</span>
  </div>
  <div class="abs en" style="left:1140px;top:40px;writing-mode:vertical-rl;font-weight:700;font-size:16px;letter-spacing:2px">↑ Go To Top</div>
  <div class="abs" style="left:40px;top:225px;font-size:12px;color:var(--muted)">© TOBIKENZAI All rights reserved.</div>
</footer>

</body>
</html>
```